Bookkeeping website design

We need a basic site design for wordpress.
We are a bookkeeping business and will need to present a look consistent with the colours and style of the logo.

Target Market(s)

Business owners

Industry/Entity Type

Accounting/Bookkeeping

Coding

Coded - Design and coding required

Number of Pages Required

1 page

```html
<!DOCTYPE html>
<html lang="en">
<head>
<meta charset="utf-8">
<title>Tallywise Bookkeeping</title>
<link href="https://fonts.googleapis.com/css2?family=Montserrat:wght@400;500;600;700;800&display=swap" rel="stylesheet">
<style>
:root{
  --blue:#19b4f0;
  --blue-deep:#1790e8;
  --green:#8cc63f;
  --ink:#1c1c1c;
  --text:#2a2a2a;
  --line:#c9ced3;
  --footer:#333435;
  --footer-text:#d8d8d8;
  --white:#ffffff;
}
*{box-sizing:border-box;margin:0;padding:0}
html,body{width:1200px;height:3229px;overflow:hidden;background:var(--white)}
body{position:relative;font-family:'Montserrat',Arial,sans-serif;color:var(--text)}
.abs{position:absolute}
.fill{position:absolute;left:0;top:0;width:100%;height:100%}

/* header */
.site-header{position:absolute;left:0;top:0;width:1200px;height:86px;background:var(--white)}
.brand{position:absolute;left:133px;top:31px;display:flex;align-items:center;gap:8px;font-weight:700;font-size:14px;color:var(--blue);white-space:nowrap}
.brand-mark{width:20px;height:20px;background:var(--green);flex:none}
.main-nav{position:absolute;left:378px;top:34px;font-size:14.5px;font-weight:500;color:var(--ink)}
.main-nav a{color:inherit;text-decoration:none;position:absolute;white-space:nowrap;top:0}
.main-nav .active{color:var(--blue);font-weight:700;border:2px solid var(--blue);padding:3px 8px;top:-6px}
.call{position:absolute;left:870px;top:24px;width:200px;height:36px}
.call-label{position:absolute;left:52px;top:0;font-size:11px;font-weight:500;color:var(--ink);white-space:nowrap}
.call-number{position:absolute;left:52px;top:12px;font-size:22px;line-height:26px;font-weight:700;color:var(--green);white-space:nowrap}

/* hero */
.hero{position:absolute;left:0;top:86px;width:1200px;height:591px}
.hero-bg{background:linear-gradient(160deg,#eef0ee 0%,#d7d9d4 35%,#8b97a6 65%,#40506a 100%)}
.hero-title{position:absolute;left:0;top:50px;width:1200px;text-align:center;font-weight:800;font-size:32px;line-height:37px}
.hero-title .l1{color:var(--ink)}
.hero-title .l2{color:var(--blue)}
.hero-title .l3{color:var(--green)}
.btn{display:inline-block;background:var(--blue);color:var(--white);font-weight:700;text-transform:uppercase;text-align:center;white-space:nowrap}
.hero .btn{position:absolute;left:533px;top:180px;width:134px;height:40px;line-height:40px;font-size:15px}
.slide-arrow{position:absolute;top:277px;width:35px;height:38px;background:var(--white);display:flex;align-items:center;justify-content:center}

/* about */
.about-kicker{position:absolute;left:131px;top:733px;font-size:19px;font-weight:500;color:var(--ink)}
.about-title{position:absolute;left:131px;top:756px;font-size:29px;font-weight:700;color:var(--blue);white-space:nowrap}
.rule{position:absolute;height:2px;background:var(--line)}
.copy{position:absolute;font-size:13.4px;line-height:21px;color:var(--text)}
.copy p{margin-bottom:21px}
.photo{position:absolute}

/* services */
.services-band{position:absolute;left:0;top:1262px;width:1200px;height:512px}
.services-bg{background:linear-gradient(90deg,#8a5a34 0%,#b9774a 40%,#cf7e42 65%,#e2894a 100%)}
.services-panel{position:absolute;left:549px;top:54px;width:579px;height:413px;background:var(--white)}
.services-title{position:absolute;left:0;top:38px;width:100%;text-align:center;font-size:23px;font-weight:700;color:var(--ink)}
.service{position:absolute;width:166px;height:127px;border:1px solid #c4c4c4;text-align:center;font-size:12px;line-height:14px;font-weight:500;color:var(--ink);text-transform:uppercase}
.service svg{display:block;margin:22px auto 10px}

/* specialist */
.spec-title{position:absolute;left:131px;top:1826px;font-size:27.5px;line-height:38px;font-weight:700;color:var(--ink);white-space:nowrap}
.spec-btn{position:absolute;left:132px;top:2332px;width:210px;height:38px;line-height:38px;font-size:13.5px}

/* contact */
.contact{position:absolute;left:0;top:2437px;width:1200px;height:448px}
.contact-bg{background:linear-gradient(90deg,#1e8fe6 0%,#1aa6f2 45%,#1593ea 100%)}
.contact-title{position:absolute;left:0;top:35px;width:100%;text-align:center;color:var(--white);font-size:29px;font-weight:700}
.contact .rule{background:var(--white);left:568px;top:82px;width:64px}
.field{position:absolute;background:var(--white);color:#444;font-size:14px;padding:15px 16px}
.submit{position:absolute;left:537px;top:353px;width:126px;height:50px;border:3px solid var(--white);color:var(--white);font-size:19px;font-weight:700;text-align:center;line-height:44px}

/* footer */
.site-footer{position:absolute;left:0;top:2885px;width:1200px;height:344px;background:var(--footer);color:var(--footer-text)}
.footer-brand{position:absolute;left:130px;top:88px;display:flex;align-items:center;gap:12px;font-weight:800;font-size:26px;color:var(--blue)}
.footer-brand .brand-mark{width:34px;height:34px}
.f-head{position:absolute;top:44px;font-size:12.5px;font-weight:700;color:var(--white)}
.f-links{position:absolute;left:496px;top:83px;font-size:11.5px;line-height:20px}
.f-item{position:absolute;font-size:11.5px;line-height:15px;white-space:nowrap}
.f-icon{position:absolute;width:22px;height:22px;border-radius:50%;background:var(--white)}
.f-icon svg{position:absolute;left:5px;top:5px}
.f-rule{position:absolute;left:133px;top:263px;width:934px;height:1px;background:#4c4d4e}
.copyright{position:absolute;left:0;top:307px;width:100%;text-align:center;font-size:9.5px}
</style>
</head>
<body>

<header class="site-header">
  <div class="brand"><span class="brand-mark"></span>Tallywise Bookkeeping</div>
  <nav class="main-nav">
    <a class="active" style="left:0">HOME</a>
    <a style="left:95px">ABOUT US</a>
    <a style="left:215px">OUR SERVICES</a>
    <a style="left:368px">CONTACT US</a>
  </nav>
  <div class="call">
    <svg class="abs" style="left:0;top:3px" width="30" height="30" viewBox="0 0 30 30" fill="none" stroke="#19b4f0" stroke-width="1.6">
      <path d="M6 4l5 1 2 6-3 2c1.5 3.5 4 6 7.5 7.5l2-3 6 2 1 5c-1 2-3 3-5 3C12 26 4 18 3.5 8.5 3.5 6.5 4.5 4.5 6 4z"/>
      <path d="M17 4a9 9 0 0 1 9 9M17 8a5 5 0 0 1 5 5"/>
    </svg>
    <div class="abs" style="left:39px;top:2px;width:2px;height:32px;background:#19b4f0"></div>
    <div class="call-label">CALL US</div>
    <div class="call-number">0400 123 456</div>
  </div>
</header>

<section class="hero">
  <div class="fill hero-bg" role="img" aria-label="Photo of two people reviewing financial charts with a calculator and pen at a desk"></div>
  <h1 class="hero-title">
    <span class="l1">LET US DO WHAT WE DO BEST,</span><br>
    <span class="l2">SO THAT YOU CAN GET ON</span><br>
    <span class="l3">WITH WHAT YOU DO BEST</span>
  </h1>
  <span class="btn">Read More</span>
  <div class="slide-arrow" style="left:0"><svg width="10" height="14" viewBox="0 0 10 14"><path d="M7 2L2 7l5 5" fill="none" stroke="#222" stroke-width="1.6"/></svg></div>
  <div class="slide-arrow" style="left:1165px"><svg width="10" height="14" viewBox="0 0 10 14"><path d="M3 2l5 5-5 5" fill="none" stroke="#222" stroke-width="1.6"/></svg></div>
</section>

<section class="about">
  <div class="about-kicker">ABOUT</div>
  <h2 class="about-title">TALLYWISE BOOKKEEPING</h2>
  <div class="rule" style="left:131px;top:797px;width:137px"></div>
  <div class="copy" style="left:134px;top:824px;width:415px">
    <p>Tallywise Bookkeeping is an offsite bookkeeping service for small to medium business’s who prefer to outsource their bookkeeping. We are located in the Northern Suburbs of Perth and service areas from Gin Gin to Joondalup.</p>
    <p>With over 30 years experience and continual ongoing education, your business will be kept up to date with the latest in legislative changes, modern awards and compliance issues.</p>
    <p>With todays technology we can offer professional bookkeeping without any disruption to your office. The added bonus is you don’t have to cover an employee for annual leave, personal leave, sick leave and even in some cases maternity leave.</p>
  </div>
  <span class="btn abs" style="left:133px;top:1167px;width:118px;height:35px;line-height:35px;font-size:13px">Read More</span>
  <div class="photo" role="img" aria-label="Photo of hands with a calculator and pen over bar charts beside a laptop" style="left:589px;top:734px;width:478px;height:470px;background:linear-gradient(170deg,#dfe6ee 0%,#b8c7d8 45%,#6f86a6 100%)"></div>
</section>

<section class="services-band">
  <div class="fill services-bg" role="img" aria-label="Photo of a wooden desk with laptop, calculator and coffee, with an orange network-line backdrop"></div>
  <div class="services-panel">
    <h2 class="services-title">OUR SERVICES</h2>
    <div class="service" style="left:32px;top:99px">
      <svg width="40" height="40" viewBox="0 0 40 40" fill="none" stroke="#19b4f0" stroke-width="2.2"><path d="M22 8H8v24h24V18"/><path d="M28 5l6 6-14 14h-6v-6z"/></svg>BAS / IAS</div>
    <div class="service" style="left:210px;top:99px">
      <svg width="40" height="40" viewBox="0 0 40 40" fill="none" stroke="#19b4f0" stroke-width="2.2"><path d="M8 4h16l6 6v24H8z"/><path d="M13 15h12M13 20h12M13 25h8"/><circle cx="31" cy="31" r="6" fill="#fff"/><path d="M31 28v6M29 29.5h3"/></svg>PAYROLL<br>SERVICES</div>
    <div class="service" style="left:388px;top:99px">
      <svg width="40" height="40" viewBox="0 0 40 40" fill="none" stroke="#19b4f0" stroke-width="2.2"><path d="M5 13L20 5l15 8z"/><path d="M8 16v14M14 16v14M20 16v14M26 16v14M32 16v14M5 33h30M4 36h32"/></svg>BANK<br>RECONCILIATION</div>
    <div class="service" style="left:32px;top:242px">
      <svg width="40" height="40" viewBox="0 0 40 40" fill="none" stroke="#19b4f0" stroke-width="2.2"><path d="M24 34H6V4h16l6 6v8"/><path d="M11 12h8M11 17h10M11 22h6"/><circle cx="28" cy="27" r="5"/><path d="M32 31l5 5"/></svg>FINANCIAL<br>REPORTING</div>
    <div class="service" style="left:210px;top:242px">
      <svg width="40" height="40" viewBox="0 0 40 40" fill="none" stroke="#19b4f0" stroke-width="2.2"><circle cx="24" cy="12" r="8"/><path d="M24 8v8M22 10h3"/><path d="M4 26h8l8 3h8l6-4M4 34h8l8 2 14-8"/></svg>AC’S PAYABLE/<br>RECEIVABLE</div>
    <div class="service" style="left:388px;top:242px">
      <svg width="40" height="40" viewBox="0 0 40 40" fill="none" stroke="#19b4f0" stroke-width="2.2"><circle cx="20" cy="20" r="7"/><path d="M20 16v8M18 18h3"/><circle cx="20" cy="5" r="2.5"/><circle cx="20" cy="35" r="2.5"/><circle cx="5" cy="20" r="2.5"/><circle cx="35" cy="20" r="2.5"/><circle cx="9" cy="9" r="2.5"/><circle cx="31" cy="9" r="2.5"/><circle cx="9" cy="31" r="2.5"/><circle cx="31" cy="31" r="2.5"/></svg>STATE<br>REVENUE PRT</div>
  </div>
</section>

<section class="specialist">
  <h2 class="spec-title">LEDGERLINE SPECIALIST |<br>REGISTERED BAS AGENT |<br>BOOKKEEPER FOR<br>SMALL BUSINESS</h2>
  <div class="copy" style="left:131px;top:1996px;width:400px">
    <p>We are registered BAS service providers who love to help small and medium businesses maintain their financial records and do their BAS. Need an in-house bookkeeper – but not full time?</p>
    <p>Streamline your bookkeeping with our reliable, seamless and professional service.</p>
    <p>At Tallywise Bookkeeping we believe quality costs less at the end of the day. Let’s work together to get it right the first time.</p>
    <p>Are your books out of control? Have you grown too big to manage it all yourself? We help businesses manage their bookkeeping systems regardless of size or industry.</p>
  </div>
  <span class="btn spec-btn">Call or Email Us Today</span>
  <div class="photo" role="img" aria-label="Photo of a smiling businesswoman working on a laptop in a studio office" style="left:555px;top:1834px;width:514px;height:543px;background:linear-gradient(160deg,#c7c9c6 0%,#9ea3a2 45%,#6d6f6c 80%,#d9d8d3 100%)"></div>
</section>

<section class="contact">
  <div class="fill contact-bg" role="img" aria-label="Blue-tinted photo of a business meeting behind the contact form"></div>
  <h2 class="contact-title">CONTACT US</h2>
  <div class="rule"></div>
  <div class="field" style="left:278px;top:123px;width:315px;height:50px">Name</div>
  <div class="field" style="left:607px;top:123px;width:314px;height:50px">Email</div>
  <div class="field" style="left:278px;top:185px;width:645px;height:132px">Message</div>
  <div class="submit">SUBMIT</div>
</section>

<footer class="site-footer">
  <div class="footer-brand"><span class="brand-mark"></span>Tallywise</div>

  <div class="f-head" style="left:496px">MENU</div>
  <div class="f-links">HOME<br>ABOUT US<br>OUR SERVICES<br>CONTACT US</div>

  <div class="f-head" style="left:678px">CONTACT US</div>
  <div class="f-icon" style="left:677px;top:82px"><svg width="12" height="12" viewBox="0 0 12 12"><path d="M6 1a3.5 3.5 0 0 1 3.5 3.5C9.5 7 6 11 6 11S2.5 7 2.5 4.5A3.5 3.5 0 0 1 6 1z" fill="#333"/><circle cx="6" cy="4.5" r="1.2" fill="#fff"/></svg></div>
  <div class="f-item" style="left:709px;top:82px">Pine Ridge,<br>Western Australia 6000</div>
  <div class="f-icon" style="left:677px;top:132px"><svg width="12" height="12" viewBox="0 0 12 12"><path d="M2.5 1.5l2 .5.6 2.2-1.2.9a6 6 0 0 0 3 3l.9-1.2 2.2.6.5 2c-.4.8-1.1 1.2-2 1.2C4.5 10.7 1.3 7.5 1.3 3.5c0-.9.4-1.6 1.2-2z" fill="#333"/></svg></div>
  <div class="f-item" style="left:709px;top:132px">Call Us<br>0400 123 456</div>
  <div class="f-icon" style="left:677px;top:184px"><svg width="12" height="12" viewBox="0 0 12 12"><rect x="1" y="2.5" width="10" height="7" fill="#333"/><path d="M1 3l5 3.5L11 3" stroke="#fff" fill="none"/></svg></div>
  <div class="f-item" style="left:709px;top:184px">E mail Us<br>hello@tallywisebooks.com.au</div>

  <div class="f-head" style="left:965px">FOLLOW US</div>
  <div class="f-icon" style="left:964px;top:82px"></div>
  <div class="f-item" style="left:999px;top:82px">Like us on<br>CIRCLEHUB</div>
  <div class="f-icon" style="left:964px;top:132px"></div>
  <div class="f-item" style="left:999px;top:132px">Follow us on<br>CHIRPNET</div>
  <div class="f-icon" style="left:964px;top:184px"></div>
  <div class="f-item" style="left:999px;top:184px">Follow us on<br>WORKLINK</div>

  <div class="f-rule"></div>
  <div class="copyright">Copyright © 2021 All Rights Reserved</div>
</footer>

</body>
</html>
```